velturi.org business card design

We need 2-sided business cards for velturi.org; one side will be printed in English (EN), the other in Spanish (ES); the information represnted will be the same.
We are a non-profit that aims to mentor and coach future leaders / visionaries. Our target markets are developing countries (Latin America, Africa, Asia) rather than the developed ("western") world. Our business model works by finding funding to mentor / coach a candidate. We provide several mentors / coaches per candidate which help translate the candidate's vision / dream into a path with objectives and steps.
We want the business cards to transmit our values, which are: innovation, learning / self-improvement, equality (i.e. free from discrimination), boldness, intelligence, thoughtfulness, culture, society, future, sustainability.
We recommend the designers work with these values to produce a bold and innovative design, which does not need to adhere to the traditional criteria for business cards. Please use fresh (modern) colours.

Target Market(s)

Visionaries and thought leaders all over the world, but initially in Latin America. We don't discriminate on age, sex, religion, race or any other difference between people

Industry/Entity Type

Leadership

Contact Information for Business Card

The business cards will contain one language (English / Spanish) per side. It would be nice to have some continuity between the front and the back (e.g. pattern, colours).
Each side will contain the company name, website (www.velturi.org) and a slogan / mantra (which will be provided and can be represented as a placeholder until such time). The other details will be Name, (Function), and contact details (email and phone number).

Font styles to use
Sans Serif

Colors

Designer to choose colors to be used in the design.

Requirements
Must have
• [Side A: ENGLISH --- COMPANY INFO]
• [Company Name] Velturi
• [Slogan / Mantra] Draw your path!
• [Website] velturi.org
• [Side A: ENGLISH --- PERSONAL INFO]
• [Name] Dan Pilcher
• [Job Title] Mentoring Coordinator
• [Phone / WhatsApp] +51 947 218 306
• [eMail] dan@velturi.org
• [Side B: SPANISH --- COMPANY INFO]
• [Company Name] Velturi
• [Slogan / Mantra] ¡Traza tu camino!
• [Website] velturi.org
• [Side B: SPANISH --- PERSONAL INFO]
• [Name] Daniel Pilcher
• [Job Title] Coordinador de Mentoreo
• [eMail] dan@velturi.org
• [SIDE A: ENGLISH --- Central Values]
• - Future
• - Growth
• - Leadership
• [SIDE B: SPANISH --- Central Values]
• - Futuro
• - Liderazgo
• - Crecimiento
Nice to have
• Innovative and different design. Modern and fresh. Bold and clever.
• Secondary Values (we would like represented) are:
• [SIDE A: ENGLISH --- Secondary Values]
• - Equality
• - Innovation
• - Sustainability
• [SIDE B: SPANISH --- Secondary Values]
• - Igualdad
• - Innovación
• - Sostenibilidad
Should not have
• Please note that the images I have attached to this brief are just some images that I liked while browsing for material for the website. It does not imply I want these colours or this type of design, just that I felt these images had a good feel.

```html
<!DOCTYPE html>
<html lang="en">
<head>
<meta charset="utf-8">
<title>Velturi business cards</title>
<link href="https://fonts.googleapis.com/css2?family=Lexend:wght@400;500;600;700&display=swap" rel="stylesheet">
<style>
  :root {
    --sun: #fff200;
    --magenta: #e8128c;
    --ink: #111111;
    --paper: #ffffff;
    --globe-blue: #bcd8f2;
    --stage: #e9e6e1;
  }
  * { box-sizing: border-box; margin: 0; padding: 0; }
  html, body { width: 900px; height: 1200px; overflow: hidden; }
  body {
    background: var(--stage);
    font-family: "Lexend", Arial, sans-serif;
    position: relative;
  }
  .card {
    position: absolute;
    left: 82px;
    width: 733px;
    height: 428px;
    border-radius: 22px;
    overflow: hidden;
  }
  .card--es { top: 137px; background: var(--sun); color: var(--ink); }
  .card--en { top: 633px; background: var(--magenta); color: var(--paper); }

  .brand { position: absolute; left: 40px; top: 47px; display: flex; align-items: center; }
  .brand__dot {
    width: 136px; height: 136px; border-radius: 50%;
    background: var(--globe-blue);
  }
  .brand__text { margin-left: 22px; margin-top: -6px; }
  .brand__name { font-size: 46px; font-weight: 600; letter-spacing: 0.5px; line-height: 1; }
  .brand__slogan { font-size: 18px; font-weight: 500; margin-top: 10px; letter-spacing: 0.3px; }
  .card--es .brand__slogan { color: var(--magenta); }
  .card--en .brand__slogan { color: var(--sun); font-weight: 400; }

  .person { position: absolute; left: 38px; top: 246px; }
  .person__name { font-size: 27px; font-weight: 700; letter-spacing: 0.3px; line-height: 1.1; }
  .person__role { font-size: 16px; font-weight: 500; margin-top: 3px; letter-spacing: 0.3px; }
  .card--es .person__role { color: var(--magenta); }
  .card--en .person__role { color: var(--sun); }

  .rule { position: absolute; left: 38px; right: 36px; top: 316px; height: 1px; }
  .card--es .rule { background: var(--ink); }
  .card--en .rule { background: var(--paper); }

  .contacts {
    position: absolute; left: 38px; right: 36px; top: 326px;
    display: flex; align-items: center; justify-content: space-between;
    font-size: 20px; font-weight: 400;
  }
  .contacts__item { display: flex; align-items: center; gap: 9px; }
  .contacts__sep { font-size: 17px; }
  .icon { width: 27px; height: 27px; flex: none; }

  .values { position: absolute; left: 0; bottom: 0; width: 733px; height: 40px; }
  .values__band { position: absolute; inset: 0; }
  .values__core {
    position: absolute; left: 36px; top: 8px;
    font-size: 19px; color: var(--paper); font-weight: 400;
  }
  .values__more { position: absolute; right: 36px; top: 14px; font-size: 15px; }
  .card--es .values__more { color: var(--paper); }
  .card--en .values__more { color: var(--ink); }
  .bullet { display: inline-block; width: 6px; height: 6px; border-radius: 50%; margin: 0 5px; vertical-align: middle; }
  .bullet--magenta { background: var(--magenta); }
  .bullet--sun { background: var(--sun); }
</style>
</head>
<body>

<section class="card card--es" lang="es">
  <div class="brand">
    <div class="brand__dot"></div>
    <div class="brand__text">
      <div class="brand__name">VELTURI</div>
      <div class="brand__slogan">¡TRAZA TU CAMINO!</div>
    </div>
  </div>
  <div class="person">
    <div class="person__name">DANIEL PILCHER</div>
    <div class="person__role">COORDINADOR DE MENTOREO</div>
  </div>
  <div class="rule"></div>
  <div class="contacts">
    <span class="contacts__item">
      <svg class="icon" viewBox="0 0 26 26"><circle cx="13" cy="13" r="13" fill="#e8128c"/><path d="M9 7l3 3-1.6 1.8a9 9 0 0 0 3.8 3.8L16 14l3 3-2 2C11.5 18.5 7.5 14.5 7 9z" fill="#fff200"/></svg>
      +51 947 218 306
    </span>
    <span class="contacts__sep">|</span>
    <span class="contacts__item">
      <svg class="icon" viewBox="0 0 26 26"><circle cx="13" cy="13" r="13" fill="#e8128c"/><rect x="7" y="8.5" width="12" height="9" fill="none" stroke="#fff" stroke-width="1.6"/><path d="M7 8.5l6 5 6-5" fill="none" stroke="#fff" stroke-width="1.6"/></svg>
      dan@velturi.org
    </span>
    <span class="contacts__sep">|</span>
    <span class="contacts__item">
      <svg class="icon" viewBox="0 0 26 26"><circle cx="13" cy="13" r="13" fill="#e8128c"/><circle cx="13" cy="13" r="6.5" fill="none" stroke="#fff" stroke-width="1.5"/><path d="M6.5 13h13M13 6.5c-3 3.5-3 9.5 0 13M13 6.5c3 3.5 3 9.5 0 13" fill="none" stroke="#fff" stroke-width="1.2"/></svg>
      velturi.org
    </span>
  </div>
  <div class="values">
    <svg class="values__band" viewBox="0 0 733 40" preserveAspectRatio="none">
      <polygon points="358,8 733,8 733,40 390,40" fill="#e8128c"/>
      <polygon points="342,0 354,0 392,40 380,40" fill="#fff200"/>
      <polygon points="0,0 342,0 380,40 0,40" fill="#111111"/>
    </svg>
    <div class="values__core">Futuro<span class="bullet bullet--magenta"></span>Liderazgo<span class="bullet bullet--magenta"></span>Crecimiento</div>
    <div class="values__more">Igualdad<span class="bullet bullet--sun"></span>Innovación<span class="bullet bullet--sun"></span>Sostenibilidad</div>
  </div>
</section>

<section class="card card--en" lang="en">
  <div class="brand">
    <div class="brand__dot"></div>
    <div class="brand__text">
      <div class="brand__name">VELTURI</div>
      <div class="brand__slogan">DRAW YOUR PATH!</div>
    </div>
  </div>
  <div class="person">
    <div class="person__name">DAN PILCHER</div>
    <div class="person__role">MENTORING COORDINATOR</div>
  </div>
  <div class="rule"></div>
  <div class="contacts">
    <span class="contacts__item">
      <svg class="icon" viewBox="0 0 26 26"><circle cx="13" cy="13" r="13" fill="#fff"/><path d="M9 7l3 3-1.6 1.8a9 9 0 0 0 3.8 3.8L16 14l3 3-2 2C11.5 18.5 7.5 14.5 7 9z" fill="#e8128c"/></svg>
      +51 947 218 306
    </span>
    <span class="contacts__sep">|</span>
    <span class="contacts__item">
      <svg class="icon" viewBox="0 0 26 26"><circle cx="13" cy="13" r="13" fill="#fff"/><rect x="7" y="8.5" width="12" height="9" fill="none" stroke="#e8128c" stroke-width="1.6"/><path d="M7 8.5l6 5 6-5" fill="none" stroke="#e8128c" stroke-width="1.6"/></svg>
      dan@velturi.org
    </span>
    <span class="contacts__sep">|</span>
    <span class="contacts__item">
      <svg class="icon" viewBox="0 0 26 26"><circle cx="13" cy="13" r="13" fill="#fff"/><circle cx="13" cy="13" r="6.5" fill="none" stroke="#e8128c" stroke-width="1.5"/><path d="M6.5 13h13M13 6.5c-3 3.5-3 9.5 0 13M13 6.5c3 3.5 3 9.5 0 13" fill="none" stroke="#e8128c" stroke-width="1.2"/></svg>
      velturi.org
    </span>
  </div>
  <div class="values">
    <svg class="values__band" viewBox="0 0 733 40" preserveAspectRatio="none">
      <polygon points="358,8 733,8 733,40 390,40" fill="#ffffff"/>
      <polygon points="342,0 354,0 392,40 380,40" fill="#e8128c"/>
      <polygon points="0,0 342,0 380,40 0,40" fill="#111111"/>
    </svg>
    <div class="values__core">Future<span class="bullet bullet--sun"></span>Growth<span class="bullet bullet--sun"></span>Leadership</div>
    <div class="values__more">Equality<span class="bullet bullet--magenta"></span>Innovation<span class="bullet bullet--magenta"></span>Sustainability</div>
  </div>
</section>

</body>
</html>
```